Scandinavian Online Sewing store need a flier

We need a 'flier' or over sized business card to include with orders which are shipped to customers. We are based in Norway and looking for something which will appeal to the Scandinavian market. The business name is 'Tråkroken' which in English means 'sewing cupboard'.

We are aiming for the younger market sector and stocking 'fresher' and 'younger' fabric, patterns and notions. (See Stitch by day, Walden+T, Harbour & Pike, Valdrine K etc.)

We would like a A5/A6 sized card which we could use in place of a business card. It should include the logo and perhaps a textured background (either paper or fabric).

Looking forward to see the ideas of all you amazingly creative souls!

Target Market(s)

Scandinavian home sewers who are interested in creating and design

Industry/Entity Type

Textile

Requirements
Must have
• logo (Attached to project) picture or artwork
Nice to have
• texture background

```html
<!DOCTYPE html>
<html lang="no">
<head>
<meta charset="utf-8">
<title>Tråkroken – flier</title>
<link rel="stylesheet" href="https://fonts.googleapis.com/css2?family=Anton&family=Amatic+SC:wght@700&display=swap">
<style>
  :root {
    --slate: #6d7a77;
    --brick: #a8432f;
    --aqua: #a9d8cd;
    --denim: #3f62a6;
    --cream: #dcdabd;
    --coral: #e2694a;
    --khaki: #c8c498;
    --tan: #c3a874;
    --raspberry: #d3506b;
    --linen: #dcd8b6;
    --olive: #787250;
    --moss: #7e9353;
    --blush: #e8d6c8;
    --mist: #bcd6d2;
    --card-green: #b2c684;
    --ink: #111111;
    --stitch: #ffffff;
    --tooth: 12px;
  }
  * { margin: 0; padding: 0; box-sizing: border-box; }
  html, body { width: 1200px; height: 846px; overflow: hidden; }
  body {
    position: relative;
    background-color: var(--slate);
    background-image:
      repeating-linear-gradient(0deg, rgba(255,255,255,.10) 0 1px, transparent 1px 3px),
      repeating-linear-gradient(90deg, rgba(0,0,0,.14) 0 1px, transparent 1px 3px);
  }

  /* fabric swatch: pinked top/bottom on the outer box, pinked sides on the cloth */
  .patch {
    position: absolute;
    -webkit-mask:
      conic-gradient(from 135deg at top, #0000, #000 1deg 89deg, #0000 90deg) top / var(--tooth) 51% repeat-x,
      conic-gradient(from -45deg at bottom, #0000, #000 1deg 89deg, #0000 90deg) bottom / var(--tooth) 51% repeat-x;
    mask:
      conic-gradient(from 135deg at top, #0000, #000 1deg 89deg, #0000 90deg) top / var(--tooth) 51% repeat-x,
      conic-gradient(from -45deg at bottom, #0000, #000 1deg 89deg, #0000 90deg) bottom / var(--tooth) 51% repeat-x;
  }
  .patch__cloth {
    position: absolute; inset: 0;
    background-color: var(--cloth);
    background-image:
      repeating-linear-gradient(0deg, rgba(255,255,255,.13) 0 1px, transparent 1px 3px),
      repeating-linear-gradient(90deg, rgba(0,0,0,.15) 0 1px, transparent 1px 3px),
      linear-gradient(135deg, rgba(255,255,255,.06), rgba(0,0,0,.08));
    -webkit-mask:
      conic-gradient(from 45deg at left, #0000, #000 1deg 89deg, #0000 90deg) left / 51% var(--tooth) repeat-y,
      conic-gradient(from -135deg at right, #0000, #000 1deg 89deg, #0000 90deg) right / 51% var(--tooth) repeat-y;
    mask:
      conic-gradient(from 45deg at left, #0000, #000 1deg 89deg, #0000 90deg) left / 51% var(--tooth) repeat-y,
      conic-gradient(from -135deg at right, #0000, #000 1deg 89deg, #0000 90deg) right / 51% var(--tooth) repeat-y;
  }

  .patch--cream     { left: 1136px; top: 52px;  width: 72px;  height: 752px; --cloth: var(--cream); }
  .patch--mist      { left: 224px;  top: 752px; width: 990px; height: 110px; --cloth: var(--mist); }
  .patch--aqua      { left: 236px;  top: 44px;  width: 720px; height: 212px; --cloth: var(--aqua); }
  .patch--brick     { left: 32px;   top: 48px;  width: 208px; height: 372px; --cloth: var(--brick); }
  .patch--denim     { left: 948px;  top: 52px;  width: 196px; height: 560px; --cloth: var(--denim); }
  .patch--khaki     { left: 752px;  top: 240px; width: 200px; height: 372px; --cloth: var(--khaki); }
  .patch--coral     { left: 564px;  top: 236px; width: 192px; height: 164px; --cloth: var(--coral); }
  .patch--tan       { left: 568px;  top: 392px; width: 188px; height: 208px; --cloth: var(--tan); }
  .patch--raspberry { left: 576px;  top: 592px; width: 184px; height: 176px; --cloth: var(--raspberry); }
  .patch--linen     { left: 752px;  top: 596px; width: 196px; height: 164px; --cloth: var(--linen); }
  .patch--olive     { left: 928px;  top: 600px; width: 224px; height: 168px; --cloth: var(--olive); }
  .patch--blush     { left: -12px;  top: 356px; width: 72px;  height: 268px; --cloth: var(--blush); }
  .patch--moss      { left: 32px;   top: 424px; width: 208px; height: 440px; --cloth: var(--moss); }

  .stitches { position: absolute; left: 0; top: 0; width: 1200px; height: 846px; }

  .card {
    position: absolute;
    left: 106px; top: 100px;
    width: 476px; height: 654px;
    background: var(--card-green);
    box-shadow: 3px 4px 10px rgba(0,0,0,0.3);
  }
  .card__name {
    position: absolute;
    left: 44px; top: 36px;
    font-family: "Anton", sans-serif;
    font-weight: 400;
    font-size: 96px;
    line-height: 1.1;
    color: var(--ink);
    text-transform: uppercase;
    white-space: nowrap;
  }
  .card__notions {
    position: absolute;
    left: 54px; top: 152px;
    width: 362px; height: 460px;
    background: linear-gradient(165deg, #3b3f33 0%, #5f6b4a 35%, #43483a 65%, #6f7c56 100%);
  }

  .site-url {
    position: absolute;
    left: 582px; top: 84px;
    font-family: "Amatic SC", sans-serif;
    font-weight: 700;
    font-size: 40px;
    letter-spacing: 3px;
    color: var(--ink);
    text-transform: uppercase;
    white-space: nowrap;
  }
  .tagline {
    position: absolute;
    left: 766px; top: 594px;
    width: 160px; height: 140px;
    font-family: "Amatic SC", sans-serif;
    font-weight: 700;
    color: var(--ink);
    text-transform: uppercase;
  }
  .tagline__line { position: absolute; left: 0; white-space: nowrap; line-height: 1; }
  .tagline__line--1 { top: 0;   font-size: 31px; letter-spacing: 5px; }
  .tagline__line--2 { top: 28px; font-size: 31px; letter-spacing: 5px; }
  .tagline__line--3 { top: 56px; font-size: 48px; letter-spacing: 8px; }
  .tagline__line--4 { top: 102px; font-size: 31px; letter-spacing: 5px; }
</style>
</head>
<body>
  <div class="patch patch--cream"><span class="patch__cloth"></span></div>
  <div class="patch patch--mist"><span class="patch__cloth"></span></div>
  <div class="patch patch--aqua"><span class="patch__cloth"></span></div>
  <div class="patch patch--brick"><span class="patch__cloth"></span></div>
  <div class="patch patch--denim"><span class="patch__cloth"></span></div>
  <div class="patch patch--khaki"><span class="patch__cloth"></span></div>
  <div class="patch patch--coral"><span class="patch__cloth"></span></div>
  <div class="patch patch--tan"><span class="patch__cloth"></span></div>
  <div class="patch patch--raspberry"><span class="patch__cloth"></span></div>
  <div class="patch patch--linen"><span class="patch__cloth"></span></div>
  <div class="patch patch--olive"><span class="patch__cloth"></span></div>
  <div class="patch patch--blush"><span class="patch__cloth"></span></div>
  <div class="patch patch--moss"><span class="patch__cloth"></span></div>

  <svg class="stitches" viewBox="0 0 1200 846" aria-hidden="true">
    <g fill="none" stroke="var(--stitch)" stroke-width="2" stroke-dasharray="14 9" stroke-linecap="round">
      <path d="M60 32 H1172 V812 H64 V416"/>
      <path d="M32 40 C26 120 34 200 28 300 C26 330 30 350 28 356"/>
    </g>
  </svg>

  <section class="card">
    <h1 class="card__name">Tråkroken</h1>
    <div class="card__notions" role="img" aria-label="Black and white illustration of sewing notions: thread spools, tape measure, safety pins, scissors, pincushion, bobbins, thimble and buttons"></div>
  </section>

  <p class="site-url">www.trakroken.no</p>

  <p class="tagline">
    <span class="tagline__line tagline__line--1">Fristelser</span>
    <span class="tagline__line tagline__line--2">for de som</span>
    <span class="tagline__line tagline__line--3">elsker</span>
    <span class="tagline__line tagline__line--4">å skaper</span>
  </p>
</body>
</html>
```